Business Card Design - Local Discount Club

Looking for a fun business card for a local discount club. One side should be the logo only and the other should be have :

Name
Title
Phone, Email
Website

```html
<!DOCTYPE html>
<html lang="en">
<head>
<meta charset="utf-8">
<title>Dune Harbor Pass – Business Card</title>
<link href="https://fonts.googleapis.com/css2?family=Montserrat:wght@500;700&family=Arimo:wght@400;700&display=swap" rel="stylesheet">
<style>
  :root {
    --backdrop: #e6e6e4;
    --card: #303031;
    --edge: #1f8fe0;
    --brand-blue: #2a9be8;
    --white: #ffffff;
    --muted: #e9e9e9;
    --rule: #8a8a8a;
    --hole-dark: #141414;
    --hole-grey: #5d5d5e;
  }
  * { box-sizing: border-box; margin: 0; padding: 0; }
  html, body {
    width: 1200px; height: 802px; overflow: hidden;
    background: var(--backdrop);
  }
  .canvas {
    position: relative; width: 1200px; height: 802px;
  }
  .card {
    position: absolute; top: 246px;
    width: 540px; height: 309px;
    background: var(--card);
    border-bottom: 4px solid var(--edge);
    border-left: 2px solid var(--edge);
    overflow: hidden;
  }
  .card--front { left: 45px; }
  .card--back { left: 615px; }

  .wordmark {
    position: absolute;
    display: flex; align-items: center; gap: 10px;
    font-family: "Montserrat", sans-serif;
    font-weight: 700;
    color: var(--brand-blue);
    text-transform: uppercase;
    line-height: 1.05;
  }
  .wordmark__dot {
    flex: none; border-radius: 50%; background: var(--brand-blue);
  }
  .card--front .wordmark { left: 34px; top: 118px; font-size: 26px; width: 210px; }
  .card--front .wordmark__dot { width: 12px; height: 12px; }
  .card--back .wordmark { left: 36px; top: 168px; font-size: 36px; width: 300px; }
  .card--back .wordmark__dot { width: 16px; height: 16px; }

  .divider {
    position: absolute; left: 262px; top: 70px;
    width: 1px; height: 170px; background: var(--rule);
  }
  .contact {
    position: absolute; left: 286px; top: 66px; width: 240px;
    font-family: "Arimo", sans-serif; color: var(--muted);
  }
  .contact__name {
    font-weight: 700; font-size: 17px; color: var(--brand-blue);
    text-transform: uppercase; letter-spacing: 0.2px;
  }
  .contact__title { font-size: 13px; margin-top: 2px; }
  .contact__address { font-size: 13px; line-height: 1.35; margin-top: 16px; }
  .contact__list { list-style: none; margin-top: 14px; }
  .contact__item {
    display: flex; align-items: center; gap: 8px;
    font-size: 13px; line-height: 1.6;
  }
  .contact__icon { width: 11px; height: 11px; flex: none; fill: var(--brand-blue); }

  .hole { position: absolute; border-radius: 50%; }
  .hole--large-top { left: 392px; top: 20px; width: 92px; height: 92px; background: var(--hole-dark); }
  .hole--small { left: 278px; top: 82px; width: 66px; height: 66px; background: var(--hole-dark); }
  .hole--large-grey {
    left: 374px; top: 128px; width: 130px; height: 130px;
    background: radial-gradient(circle at 40% 35%, #6d6d6e, var(--hole-grey) 60%, #3f3f40);
  }
</style>
</head>
<body>
<main class="canvas">
  <section class="card card--front" aria-label="Card front">
    <div class="wordmark"><span class="wordmark__dot"></span><span>Dune Harbor Pass</span></div>
    <div class="divider"></div>
    <div class="contact">
      <p class="contact__name">Marcus Hale</p>
      <p class="contact__title">Manager</p>
      <p class="contact__address">12 Shore Road, Harborview<br>State, Zip 00000</p>
      <ul class="contact__list">
        <li class="contact__item">
          <svg class="contact__icon" viewBox="0 0 24 24"><path d="M6.6 10.8a15 15 0 0 0 6.6 6.6l2.2-2.2a1 1 0 0 1 1-.25 11.4 11.4 0 0 0 3.6.57 1 1 0 0 1 1 1V20a1 1 0 0 1-1 1A17 17 0 0 1 3 4a1 1 0 0 1 1-1h3.5a1 1 0 0 1 1 1c0 1.25.2 2.45.57 3.57a1 1 0 0 1-.25 1z"/></svg>
          555-014-2290
        </li>
        <li class="contact__item">
          <svg class="contact__icon" viewBox="0 0 24 24"><path d="M2 5h20v14H2z M2 5l10 8 10-8" stroke="#303031" stroke-width="1.5"/></svg>
          hello@duneharborpass.com
        </li>
        <li class="contact__item">
          <svg class="contact__icon" viewBox="0 0 24 24"><circle cx="12" cy="12" r="10"/><path d="M2 12h20M12 2c3 3 3 17 0 20M12 2c-3 3-3 17 0 20" stroke="#303031" stroke-width="1.5" fill="none"/></svg>
          www.duneharborpass.com
        </li>
      </ul>
    </div>
  </section>

  <section class="card card--back" aria-label="Card back">
    <div class="hole hole--large-top"></div>
    <div class="hole hole--small"></div>
    <div class="hole hole--large-grey"></div>
    <div class="wordmark"><span class="wordmark__dot"></span><span>Dune Harbor Pass</span></div>
  </section>
</main>
</body>
</html>
```